Redesign of business card for Birchline Mechanical

We are looking for a new design for our business cards for Birchline Mechanical. We are a plumbing & HVAC construction company, operating on the West Coast of Canada and USA. Logo attached.
Industry/Entity Type
Construction - Plumbing & HVAC
Contact Information for Business Card
Name, address, phone numbers, email, website address
Look and feel
Each slider illustrates characteristics of the customer's brand and the style your logo design should communicate.

```html
<!DOCTYPE html>
<html lang="en">
<head>
<meta charset="utf-8">
<title>Birchline Mechanical – Business Card</title>
<link href="https://fonts.googleapis.com/css2?family=Montserrat:wght@300;400;600;700&family=Open+Sans:wght@400&display=swap" rel="stylesheet">
<style>
  :root {
    --ink: #231f20;
    --paper: #ffffff;
    --backdrop: #d9d6d2;
    --rule: #231f20;
  }
  * { box-sizing: border-box; margin: 0; padding: 0; }
  html, body { width: 1200px; height: 900px; overflow: hidden; }
  body {
    background: var(--backdrop);
    position: relative;
    font-family: "Open Sans", sans-serif;
    color: var(--ink);
  }
  .card {
    position: absolute;
    left: 250px;
    width: 700px;
    height: 400px;
    box-shadow: 0 6px 18px rgba(0,0,0,.25);
    overflow: hidden;
  }
  .card-front { top: 40px; background: var(--ink); }
  .card-back { top: 460px; background: var(--paper); }

  .brand {
    position: absolute;
    display: flex;
    align-items: center;
    gap: 14px;
    font-family: "Montserrat", sans-serif;
    font-weight: 600;
    text-transform: uppercase;
    letter-spacing: 2px;
    white-space: nowrap;
  }
  .brand-mark { display: block; border: 5px solid currentColor; }
  .card-front .brand {
    color: var(--paper);
    left: 50%; top: 50%;
    transform: translate(-50%, -50%);
    font-size: 30px;
  }
  .card-front .brand-mark { width: 44px; height: 44px; }
  .card-back .brand {
    color: var(--ink);
    right: 50px; top: 48px;
    font-size: 20px;
  }
  .card-back .brand-mark { width: 32px; height: 32px; border-width: 4px; }

  .logo-rule {
    position: absolute;
    left: 330px; right: 40px; top: 128px;
    height: 2px; background: var(--rule);
  }
  .address {
    position: absolute;
    right: 40px; top: 150px;
    text-align: right;
    font-size: 17px;
    line-height: 1.35;
  }
  .holder {
    position: absolute;
    left: 40px; top: 212px;
    font-family: "Montserrat", sans-serif;
  }
  .holder-name { font-weight: 700; font-size: 26px; letter-spacing: 1px; }
  .holder-title { font-weight: 300; font-size: 17px; letter-spacing: 1.5px; margin-top: 2px; }
  .holder-rule {
    position: absolute;
    left: 40px; top: 290px; width: 240px;
    height: 2px; background: var(--rule);
  }
  .contact-list {
    position: absolute;
    left: 40px; top: 302px;
    list-style: none;
    font-size: 17px;
    line-height: 1.7;
  }
  .contact-list li { display: flex; align-items: center; gap: 12px; }
  .contact-list svg { width: 18px; height: 18px; fill: var(--ink); }

  .footer-art { position: absolute; left: 0; bottom: 0; width: 700px; height: 70px; }
  .website {
    position: absolute;
    right: 40px; bottom: 32px;
    color: var(--paper);
    font-size: 16px;
    letter-spacing: .5px;
  }
</style>
</head>
<body>
  <section class="card card-front">
    <div class="brand"><span class="brand-mark"></span>Birchline Mechanical</div>
  </section>

  <section class="card card-back">
    <div class="brand"><span class="brand-mark"></span>Birchline Mechanical</div>
    <div class="logo-rule"></div>

    <address class="address" style="font-style:normal">
      421, Address line goes here<br>
      45452, Country name
    </address>

    <div class="holder">
      <div class="holder-name">JONATHAN SMITH</div>
      <div class="holder-title">MANAGING DIRECTOR</div>
    </div>
    <div class="holder-rule"></div>

    <ul class="contact-list">
      <li>
        <svg viewBox="0 0 24 24" aria-hidden="true"><path d="M6.6 10.8a15.1 15.1 0 0 0 6.6 6.6l2.2-2.2c.3-.3.7-.4 1-.2 1.1.4 2.3.6 3.6.6.6 0 1 .4 1 1V20c0 .6-.4 1-1 1A17 17 0 0 1 3 4c0-.6.4-1 1-1h3.5c.6 0 1 .4 1 1 0 1.3.2 2.5.6 3.6.1.3 0 .7-.2 1z"/></svg>
        044-123 456 789
      </li>
      <li>
        <svg viewBox="0 0 24 24" aria-hidden="true"><path d="M2 5h20v14H2z M2 5l10 8 10-8" fill="none" stroke="#231f20" stroke-width="2.4"/><path d="M2 5h20l-10 8z"/></svg>
        info@webname.com
      </li>
    </ul>

    <svg class="footer-art" viewBox="0 0 700 70" aria-hidden="true">
      <path d="M430 14 H700 V50 H405 Z" fill="#231f20"/>
      <path d="M0 56 H398 L422 22 H700 V26 H424 L400 60 H0 Z" fill="#231f20"/>
      <rect x="0" y="63" width="700" height="7" fill="#231f20"/>
    </svg>
    <div class="website">www.websitename.com</div>
  </section>
</body>
</html>
```